Stationery Design Project

We need a stationery design for a consultancy called 'Marlow Ridge'. The design should communicate innovation and professionalism. The colors used should complement our logo. Please include source files for winning design.

Requirements
Must have
• Logo with company name should be included. Font of the text in logo should not be altered. Paper should be A4 sized and not Letter sized.

```html
<!DOCTYPE html>
<html lang="en">
<head>
<meta charset="utf-8">
<title>Marlow Ridge Stationery</title>
<link href="https://fonts.googleapis.com/css2?family=Cinzel:wght@400;600&family=Open+Sans:wght@400;600&display=swap" rel="stylesheet">
<style>
:root{
  --board:#eeeeee;
  --paper:#ffffff;
  --orange:#f7941d;
  --orange-soft:#fbd3a4;
  --black:#141414;
  --ink:#555555;
  --caption:#8a8a8a;
  --shadow:0 3px 8px rgba(0,0,0,.22);
}
*{box-sizing:border-box;margin:0;padding:0}
html,body{width:1200px;height:480px;overflow:hidden}
body{background:var(--board);font-family:"Open Sans",Arial,sans-serif;position:relative}
.item{position:absolute;box-shadow:var(--shadow);overflow:hidden}
.caption{position:absolute;font-size:9px;color:var(--caption);text-align:center}
.brand{font-family:"Cinzel",Georgia,serif;font-weight:400;letter-spacing:.04em;text-transform:uppercase}
.mark{border-radius:50%;background:var(--orange);display:block}

/* letterheads */
.letterhead{background:var(--paper)}
.letterhead .head{position:absolute;left:0;right:0;top:8px;display:flex;flex-direction:column;align-items:center;gap:2px}
.letterhead .head .mark{width:15px;height:15px}
.letterhead .head .brand{font-size:5px;color:var(--orange)}
.letter{position:absolute;left:14px;right:14px;top:50px;font-size:3.2px;line-height:1.5;color:var(--ink)}
.letter p{margin-bottom:4px}
.letter .sign{margin-top:6px}
.faint-mark{position:absolute;width:80px;height:80px;border-radius:50%;background:var(--orange);opacity:.14;left:22px;bottom:18px}
.lh1-foot{position:absolute;left:0;right:0;bottom:6px;font-size:3px;color:var(--ink);text-align:center}
.lh2-foot{position:absolute;left:0;right:0;bottom:9px;height:9px;background:var(--orange);font-size:3px;color:var(--black);display:flex;align-items:center;justify-content:center}

/* folders */
.folder1{background:var(--orange)}
.folder1 .band{position:absolute;left:0;right:0;top:109px;height:57px;background:var(--black)}
.folder1 .mark{position:absolute;left:52px;top:101px;width:76px;height:76px;border:3px solid var(--black)}
.folder1 .brand{position:absolute;left:0;right:0;top:174px;text-align:center;font-size:19px;color:var(--black)}
.folder1 .faint-mark{left:44px;top:228px;bottom:auto;width:92px;height:92px;background:#fff;opacity:.12}
.folder2{background:var(--black)}
.folder2 .mark{position:absolute;left:59px;top:128px;width:84px;height:84px}
.folder2 .brand{position:absolute;left:0;right:0;top:224px;text-align:center;font-size:19px;color:#fff}

/* business cards */
.card{display:flex;align-items:center;justify-content:center}
.card-front{background:var(--orange)}
.card-front .band{position:absolute;left:0;right:0;top:14px;height:20px;background:var(--black)}
.card-front .mark{position:relative;width:22px;height:22px;border:2px solid var(--black)}
.card-back{background:var(--orange);flex-direction:column;gap:1px;font-size:4px;color:var(--black)}
.card-back .band{position:absolute;left:0;right:0;top:20px;height:14px;background:var(--black)}
.card-back .mark{position:relative;width:16px;height:16px;border:2px solid var(--black)}
.card-back .details{position:absolute;bottom:4px;left:0;right:0;text-align:center;font-size:3.5px}
.card-dark{background:var(--black);flex-direction:column;gap:3px}
.card-dark .mark{width:18px;height:18px}
.card-dark .brand{font-size:5px;color:#fff}

/* envelopes */
.envelope{background:var(--paper)}
.env-front .logo{position:absolute;left:8px;top:7px;display:flex;align-items:center;gap:3px}
.env-front .mark{width:10px;height:10px}
.env-front .brand{font-size:4px;color:var(--orange)}
.env-back svg{position:absolute;left:0;top:0}
.env-back .mark{position:absolute;left:95px;top:20px;width:22px;height:22px;border:2px solid var(--black)}
</style>
</head>
<body>

<!-- Letter head 1 -->
<section class="item letterhead" style="left:240px;top:28px;width:151px;height:303px">
  <div class="head"><span class="mark"></span><span class="brand">Marlow Ridge</span></div>
  <div class="faint-mark" aria-hidden="true"></div>
  <div class="letter">
    <p>12 May 2024</p>
    <p>Dear Client,</p>
    <p>Thank you for your interest in our consultancy services. We look forward to working with you on the coming project and sharing our ideas.</p>
    <p>Our team has prepared a short outline of the next steps, timing and costs for your review.</p>
    <p>Please contact us with any questions. We will be glad to meet at your convenience.</p>
    <p class="sign">Kind regards,<br>Anna Brooks<br>Managing Director</p>
  </div>
  <div class="lh1-foot">12 Harbour Lane, Westport · +1 555 0142 · hello@marlowridge.com</div>
</section>
<div class="caption" style="left:240px;top:339px;width:151px">Letter head 1</div>

<!-- Folder 1 -->
<section class="item folder1" style="left:472px;top:23px;width:180px;height:302px">
  <div class="band"></div>
  <span class="mark"></span>
  <div class="brand">Marlow Ridge</div>
</section>
<div class="caption" style="left:472px;top:337px;width:180px">Folder 1</div>

<!-- Letter head 2 -->
<section class="item letterhead" style="left:699px;top:28px;width:180px;height:293px">
  <div class="head"><span class="mark"></span><span class="brand">Marlow Ridge</span></div>
  <div class="letter" style="top:52px">
    <p>Dear Client,</p>
    <p>Thank you for your interest in our consultancy services. We look forward to working with you on the coming project and sharing our ideas.</p>
    <p>Please contact us with any questions. We will be glad to meet at your convenience.</p>
    <p class="sign">Kind regards,</p>
  </div>
  <div class="lh2-foot">12 Harbour Lane, Westport · +1 555 0142 · hello@marlowridge.com</div>
</section>
<div class="caption" style="left:699px;top:333px;width:180px">Letter head 2</div>

<!-- Folder 2 -->
<section class="item folder2" style="left:926px;top:19px;width:202px;height:302px">
  <span class="mark"></span>
  <div class="brand">Marlow Ridge</div>
</section>
<div class="caption" style="left:926px;top:333px;width:202px">Folder 2</div>

<!-- Business cards -->
<section class="item card card-front" style="left:9px;top:352px;width:99px;height:48px">
  <div class="band"></div><span class="mark"></span>
</section>
<div class="caption" style="left:9px;top:404px;width:99px;font-size:5px">Business Card Front</div>

<section class="item card card-back" style="left:113px;top:333px;width:85px;height:50px">
  <div class="band"></div><span class="mark"></span>
  <div class="details">Anna Brooks · Consultant · +1 555 0142</div>
</section>
<div class="caption" style="left:113px;top:385px;width:85px;font-size:5px">Business Card Back</div>

<section class="item card card-dark" style="left:113px;top:393px;width:85px;height:50px">
  <span class="mark"></span><span class="brand">Marlow Ridge</span>
</section>

<!-- Envelope front -->
<section class="item envelope env-front" style="left:227px;top:340px;width:211px;height:108px">
  <div class="logo"><span class="mark"></span><span class="brand">Marlow Ridge</span></div>
</section>
<div class="caption" style="left:227px;top:458px;width:211px">Envelope Front</div>

<!-- Envelope back -->
<section class="item envelope env-back" style="left:467px;top:340px;width:211px;height:108px">
  <svg width="211" height="108" viewBox="0 0 211 108" aria-hidden="true">
    <path d="M0 0 H211 V14 Q106 70 0 14 Z" fill="#141414"/>
    <path d="M0 108 L92 58 Q106 52 119 58 L211 108" fill="none" stroke="#dddddd" stroke-width="1"/>
  </svg>
  <span class="mark"></span>
</section>
<div class="caption" style="left:467px;top:458px;width:211px">Envelope Back</div>

</body>
</html>
```